Corporate Business Card

Very professional, Modern, Not to busy, include phone address email, website
(253) 555-0174, 61807 19th Street N, Kent, WA 98517, marcus@kestrelbayholding.com, brelvanindustries.com

Target Market(s)

Manufacturing

Industry/Entity Type

Aero, machining, manufacturing, Off road racing

Contact Information for Business Card

Phone, address email, website

```html
<!DOCTYPE html>
<html lang="en">
<head>
<meta charset="utf-8">
<title>Brelvan Industries – Business Card</title>
<link href="https://fonts.googleapis.com/css2?family=Roboto:wght@300;400;500;700;900&display=swap" rel="stylesheet">
<style>
  :root {
    --backdrop: #b2cfe8;
    --navy: #16346b;
    --navy-deep: #133064;
    --red: #d9252a;
    --paper: #ffffff;
  }
  * { margin: 0; padding: 0; box-sizing: border-box; }
  html, body { width: 1200px; height: 1200px; overflow: hidden; }
  body {
    background: var(--backdrop);
    font-family: "Roboto", Arial, sans-serif;
    position: relative;
  }
  .card {
    position: absolute;
    left: 278px;
    width: 644px;
    height: 386px;
  }
  .card--back { top: 158px; background: var(--navy); }
  .card--front { top: 643px; background: var(--paper); }

  .back-pattern {
    position: absolute;
    inset: 12px 8px;
    background: var(--navy-deep);
    opacity: 0.6;
  }
  .back-brand {
    position: absolute;
    left: 0; right: 0; top: 176px;
    text-align: center;
    color: var(--paper);
    font-weight: 900;
    font-size: 22px;
    letter-spacing: 1px;
    line-height: 1;
  }
  .back-brand small {
    display: block;
    font-size: 8px;
    letter-spacing: 2px;
    margin-top: 4px;
  }

  .front-brand {
    position: absolute;
    left: 0; right: 0; top: 34px;
    text-align: center;
    color: var(--navy);
    font-weight: 900;
    line-height: 1;
  }
  .front-brand .brand-name { display: block; font-size: 48px; letter-spacing: 2px; }
  .front-brand .brand-sub { display: block; font-size: 15px; letter-spacing: 4px; margin-top: 8px; }

  .tricolor-rule {
    position: absolute;
    left: 118px; top: 124px;
    width: 424px; height: 4px;
    display: flex;
  }
  .tricolor-rule .seg-red { width: 78px; background: var(--red); }
  .tricolor-rule .seg-navy { flex: 1; background: var(--navy); }

  .identity { position: absolute; left: 50px; top: 180px; width: 182px; }
  .identity .role {
    color: var(--navy);
    font-weight: 500;
    font-size: 18px;
    padding: 0 0 4px 3px;
    border-bottom: 1.5px solid var(--navy);
  }
  .identity .person {
    color: var(--red);
    font-weight: 500;
    font-size: 26px;
    margin: 6px 0 0 3px;
  }

  .divider {
    position: absolute;
    left: 283px; top: 167px;
    width: 1.5px; height: 177px;
    background: var(--red);
  }

  .contact-list { position: absolute; left: 314px; top: 188px; list-style: none; }
  .contact-list li {
    display: flex;
    align-items: flex-start;
    color: var(--navy);
    font-weight: 300;
    font-size: 18.5px;
    line-height: 23px;
    margin-bottom: 9px;
  }
  .contact-list svg {
    width: 16px; height: 16px;
    flex: none;
    margin: 4px 22px 0 0;
    stroke: var(--red);
    fill: none;
    stroke-width: 1.4;
  }
</style>
</head>
<body>
  <section class="card card--back" aria-label="Card back">
    <div class="back-pattern" role="img" aria-label="Faint repeating brand pattern in navy"></div>
    <div class="back-brand">BRELVAN<small>INDUSTRIES</small></div>
  </section>

  <section class="card card--front" aria-label="Card front">
    <div class="front-brand">
      <span class="brand-name">BRELVAN</span>
      <span class="brand-sub">INDUSTRIES</span>
    </div>
    <div class="tricolor-rule"><span class="seg-red"></span><span class="seg-navy"></span><span class="seg-red"></span></div>

    <div class="identity">
      <p class="role">Owner</p>
      <p class="person">Your Name</p>
    </div>

    <div class="divider"></div>

    <ul class="contact-list">
      <li>
        <svg viewBox="0 0 16 16"><path d="M8 15s5-5 5-8.5A5 5 0 0 0 3 6.5C3 10 8 15 8 15z"/><circle cx="8" cy="6.5" r="1.6"/></svg>
        <span>61807 19th Street N, Kent,<br>WA 98517,</span>
      </li>
      <li>
        <svg viewBox="0 0 16 16"><path d="M3 1.5h3l1.2 3-1.7 1.2a8 8 0 0 0 4.8 4.8l1.2-1.7 3 1.2v3a1.5 1.5 0 0 1-1.6 1.5A12.5 12.5 0 0 1 1.5 3.1 1.5 1.5 0 0 1 3 1.5z"/></svg>
        <span>(253) 555-0174</span>
      </li>
      <li>
        <svg viewBox="0 0 16 16"><rect x="1.5" y="3.5" width="13" height="9"/><path d="M1.5 3.5 8 9l6.5-5.5"/></svg>
        <span>marcus@kestrelbayholding.com</span>
      </li>
      <li>
        <svg viewBox="0 0 16 16"><circle cx="8" cy="8" r="6.5"/><ellipse cx="8" cy="8" rx="2.8" ry="6.5"/><path d="M1.5 8h13M2.5 4.8h11M2.5 11.2h11"/></svg>
        <span>brelvanindustries.com</span>
      </li>
    </ul>
  </section>
</body>
</html>
```